Zielgruppe
Steuerberatung
Aufgabenstellung
Ich benötige eine Neuerstellung für ein vorhandenes Briefpapier. Bedeutet, eigentlich soll der aktuelle Inhalt neu erstellt werden, da mir die Rohdaten nicht mehr zur Verfügung stehen. Das aktuelle Briefpapier steht als .doc zur Verfügung. Ziel 1:1 Abbildung. Zudem muss die Adresse geändert werden.

```html
<!DOCTYPE html>
<html lang="de">
<head>
<meta charset="utf-8">
<title>Briefpapier – Lukas Brenner Steuerberater</title>
<link rel="stylesheet" href="https://fonts.googleapis.com/css2?family=Libre+Franklin:wght@400;600&display=swap">
<style>
  :root {
    --paper: #ffffff;
    --ink: #333333;
    --ink-soft: #4a4a4a;
    --rule: #555555;
  }
  * { margin: 0; padding: 0; box-sizing: border-box; }
  html, body {
    width: 1198px;
    height: 1200px;
    overflow: hidden;
    background: var(--paper);
    font-family: "Libre Franklin", Arial, sans-serif;
    color: var(--ink);
  }
  .letterhead {
    position: relative;
    width: 1198px;
    height: 1200px;
  }
  .brand {
    position: absolute;
    left: 110px;
    top: 230px;
    display: flex;
    align-items: center;
    gap: 34px;
  }
  .brand-mark {
    width: 150px;
    height: 150px;
    border-radius: 50%;
    background: var(--ink);
    flex: none;
  }
  .brand-name {
    font-weight: 600;
    font-size: 64px;
    line-height: 1.05;
    color: var(--ink);
    letter-spacing: -0.5px;
  }
  .sender {
    position: absolute;
    left: 110px;
    top: 520px;
    padding-left: 34px;
    border-left: 2px solid var(--rule);
    font-size: 30px;
    line-height: 1.3;
    color: var(--ink-soft);
  }
  .sender-name { font-weight: 600; color: var(--ink); }
  .sender-divider { font-weight: 400; }
  .sender-address { margin-bottom: 34px; }
  .contact-list { list-style: none; }
  .contact-item {
    display: flex;
    align-items: center;
    gap: 18px;
  }
  .contact-icon {
    width: 24px;
    height: 24px;
    fill: var(--ink);
    flex: none;
  }
  .letter-date {
    position: absolute;
    right: 110px;
    top: 1010px;
    font-size: 36px;
    color: var(--ink);
  }
</style>
</head>
<body>
<main class="letterhead">
  <header class="brand">
    <span class="brand-mark" aria-hidden="true"></span>
    <p class="brand-name">Lukas Brenner<br>Steuerberater</p>
  </header>

  <address class="sender" style="font-style: normal;">
    <p class="sender-name">Lukas Brenner <span class="sender-divider">| Steuerberater</span></p>
    <p class="sender-address">Ahornweg 58<br>30169 Hannover</p>
    <ul class="contact-list">
      <li class="contact-item">
        <svg class="contact-icon" viewBox="0 0 24 24" aria-label="Mobil"><path d="M6.6 10.8a15.1 15.1 0 0 0 6.6 6.6l2.2-2.2a1 1 0 0 1 1-.25 11.4 11.4 0 0 0 3.6.57 1 1 0 0 1 1 1V20a1 1 0 0 1-1 1A17 17 0 0 1 3 4a1 1 0 0 1 1-1h3.5a1 1 0 0 1 1 1c0 1.25.2 2.45.57 3.6a1 1 0 0 1-.25 1z"/></svg>
        <span>+49 (0) 170 - 55 28 341</span>
      </li>
      <li class="contact-item">
        <svg class="contact-icon" viewBox="0 0 24 24" aria-label="Fax"><path d="M7 3h10v5H7z"/><path d="M4 9h16a2 2 0 0 1 2 2v6h-4v4H6v-4H2v-6a2 2 0 0 1 2-2zm4 7v3h8v-3z"/></svg>
        <span>+49 (0) 511 - 20 64 17 93</span>
      </li>
      <li class="contact-item">
        <svg class="contact-icon" viewBox="0 0 24 24" aria-label="E-Mail"><path d="M2 5h20v14H2z M3.5 6.5 12 13l8.5-6.5" stroke="#fff" stroke-width="1.6"/></svg>
        <span>info@steuerberatung-brenner.de</span>
      </li>
      <li class="contact-item">
        <svg class="contact-icon" viewBox="0 0 24 24" aria-label="Web"><circle cx="12" cy="12" r="10"/><path d="M2 12h20M12 2c3 3.2 3 16.8 0 20M12 2c-3 3.2-3 16.8 0 20" stroke="#fff" stroke-width="1.4" fill="none"/></svg>
        <span>www.steuerberatung-brenner.de</span>
      </li>
    </ul>
  </address>

  <p class="letter-date">12.03.2021</p>
</main>
</body>
</html>
```